Kestrel Business Accountants , logo & business card design

I am a business consultant & accountant , servicing a range of small business clients , providing business & taxation advice.
I am looking for a logo & business card design that is not traditional accounting style.
Something colorful & innovative would be good.
Target Market(s)
Small businesses in their growth stage
Industry/Entity Type
Business Consultant
Contact Information for Business Card
Kestrel Business Accountants Pty Ltd
Peter Lamb CPA
Director
Ph: 0491 8306 42
Email : kestrel@brindlemail.com.au
On reverse of card:
"Kestrel Insight for your Business"
Business Consulting
Taxation
Superannuation
Logo styles of interest
Abstract Logo
Wordmark Logo
Look and feel
Each slider illustrates characteristics of the customer's brand and the style your logo design should communicate.

```html
<!DOCTYPE html>
<html lang="en">
<head>
<meta charset="utf-8">
<title>Kestrel Business Accountants – Business Card</title>
<link rel="stylesheet" href="https://fonts.googleapis.com/css2?family=Roboto+Condensed:wght@700&family=Roboto:wght@700;900&display=swap">
<style>
  :root {
    --stage: #3a2a22;
    --card-base: #8c847d;
    --splash-blue: #1c96d4;
    --splash-red: #e8242b;
    --splash-lime: #c6d12a;
    --splash-magenta: #d41a8c;
    --splash-yellow: #f0b800;
    --band-pink: #d81f83;
    --ink-light: #ffffff;
    --ink-dark: #3a2a10;
  }
  * { box-sizing: border-box; margin: 0; padding: 0; }
  html, body { width: 1200px; height: 900px; overflow: hidden; }
  body {
    background: var(--stage);
    position: relative;
    font-family: "Roboto", Arial, sans-serif;
  }
  .card {
    position: absolute;
    width: 560px;
    height: 340px;
    border-radius: 18px;
    background: var(--card-base);
    overflow: hidden;
    box-shadow: 0 10px 30px rgba(0,0,0,.45);
  }
  .card--front { left: 60px; top: 70px; }
  .card--back { left: 580px; top: 490px; }
  .card svg { position: absolute; inset: 0; width: 100%; height: 100%; }
  .wordmark {
    position: absolute;
    color: var(--ink-light);
    font-family: "Roboto Condensed", Arial, sans-serif;
    font-weight: 700;
    text-transform: uppercase;
    line-height: 1.05;
    white-space: nowrap;
  }
  .wordmark__name { display: block; font-size: 26px; letter-spacing: .5px; }
  .wordmark__suffix { display: block; font-size: 10px; letter-spacing: 1px; margin-top: 3px; }
  .card--front .wordmark { left: 115px; top: 62px; }
  .card--back .wordmark { left: 140px; top: 36px; }
  .card--back .wordmark__name { font-size: 22px; }
  .tagline-band {
    position: absolute;
    background: var(--band-pink);
    color: var(--ink-light);
    font-family: "Roboto", Arial, sans-serif;
    font-weight: 700;
    font-size: 17px;
    padding: 6px 14px;
    white-space: nowrap;
  }
  .card--front .tagline-band { right: 0; bottom: 72px; }
  .card--back .tagline-band { left: 0; bottom: 26px; font-size: 19px; }
  .person {
    position: absolute;
    left: 170px;
    top: 128px;
    display: flex;
    flex-direction: column;
    align-items: flex-end;
    color: var(--ink-light);
    font-family: "Roboto Condensed", Arial, sans-serif;
    font-weight: 700;
    white-space: nowrap;
  }
  .person__line { text-transform: uppercase; }
  .person__name { font-size: 24px; letter-spacing: 1px; }
  .person__cred { font-size: 13px; margin-left: 8px; vertical-align: top; }
  .person__role { font-size: 14px; margin-right: 34px; }
  .contact {
    position: absolute;
    left: 378px;
    top: 132px;
    width: 178px;
    color: var(--ink-dark);
    font-family: "Roboto Condensed", Arial, sans-serif;
    font-weight: 700;
    font-size: 10.5px;
    line-height: 1.3;
    text-align: center;
    white-space: nowrap;
  }
  .contact__phone { display: block; margin-bottom: 30px; font-size: 11.5px; }
  .contact__email { display: block; }
</style>
</head>
<body>

<section class="card card--front" aria-label="Card front">
  <svg viewBox="0 0 560 340">
    <defs>
      <radialGradient id="gBlue" cx="50%" cy="45%" r="60%"><stop offset="0" stop-color="#2aa6e2"/><stop offset="1" stop-color="#1683c0"/></radialGradient>
      <radialGradient id="gYellow" cx="50%" cy="50%" r="60%"><stop offset="0" stop-color="#f7c400"/><stop offset="1" stop-color="#e0a800"/></radialGradient>
    </defs>
    <g role="img" aria-label="Colourful paint splatter artwork in blue, red, lime, magenta and yellow">
      <ellipse cx="260" cy="110" rx="210" ry="115" fill="url(#gBlue)"/>
      <ellipse cx="480" cy="45" rx="85" ry="65" fill="var(--splash-red)"/>
      <ellipse cx="505" cy="195" rx="80" ry="55" fill="var(--splash-magenta)"/>
      <ellipse cx="480" cy="120" rx="58" ry="46" fill="var(--splash-lime)"/>
      <ellipse cx="150" cy="262" rx="130" ry="88" fill="url(#gYellow)"/>
    </g>
  </svg>
  <div class="wordmark">
    <span class="wordmark__name">Kestrel</span>
    <span class="wordmark__name">Business Accountants</span>
    <span class="wordmark__suffix">Pty Ltd</span>
  </div>
  <div class="tagline-band">Kestrel Insight for your Business</div>
</section>

<section class="card card--back" aria-label="Card back">
  <svg viewBox="0 0 560 340">
    <defs>
      <radialGradient id="gBlue2" cx="50%" cy="45%" r="60%"><stop offset="0" stop-color="#2aa6e2"/><stop offset="1" stop-color="#1683c0"/></radialGradient>
      <radialGradient id="gYellow2" cx="50%" cy="50%" r="60%"><stop offset="0" stop-color="#f7c400"/><stop offset="1" stop-color="#e0a800"/></radialGradient>
    </defs>
    <g role="img" aria-label="Colourful paint splatter artwork in blue, red, lime, magenta and yellow">
      <ellipse cx="70" cy="95" rx="90" ry="80" fill="var(--splash-red)"/>
      <ellipse cx="265" cy="120" rx="175" ry="115" fill="url(#gBlue2)"/>
      <ellipse cx="195" cy="260" rx="105" ry="65" fill="var(--splash-magenta)"/>
      <ellipse cx="110" cy="205" rx="70" ry="55" fill="var(--splash-lime)"/>
      <ellipse cx="470" cy="170" rx="100" ry="100" fill="url(#gYellow2)"/>
    </g>
  </svg>
  <div class="wordmark">
    <span class="wordmark__name">Kestrel</span>
    <span class="wordmark__name">Business Accountants</span>
    <span class="wordmark__suffix">Pty Ltd</span>
  </div>
  <div class="person">
    <span class="person__line"><span class="person__name">Peter Lamb</span><span class="person__cred">CPA</span></span>
    <span class="person__role">Director</span>
  </div>
  <div class="contact">
    <span class="contact__phone">Ph: 0491 8306 42</span>
    <span class="contact__email">Email : kestrel@brindlemail.com.au</span>
  </div>
  <div class="tagline-band">Kestrel Insight for your Business</div>
</section>

</body>
</html>
```